Postcard Design

The business Logo is 'Brambo' it is grass cutting and maintenance. It will offer grass cutting with stripes including edging. Other services include decking/fencing maintenance, lawn treatment and patio/drive cleaning...... prices start from £10 to include front and rear lawns, Regular cuts or a one off tidy. private and commercial. Contracts welcome.
call 01642385106 or 07481926053 for a free quote.
one of the pics that i have sent is the logo (obviously it would need to be tidied up and neater) that is just rough. The other pic is one of pello cards templates but is the one that is the preferred out of all of them. If it could be similar to that with the logo on would be great.
a before (long scruffy grass) and after (neat Lawn) half and half of the postcard would be great.

Target Market(s)

Middle class home owners.

Industry/Entity Type

Business

Requirements
Must have
• The 'Brambo' logo
Nice to have
• we have a lot of junk mail posted in this area and a lot just gets put in the bin so could you make it eye catching.

```html
<!DOCTYPE html>
<html lang="en">
<head>
<meta charset="utf-8">
<title>Brambo Lawn Care – Postcard</title>
<link rel="stylesheet" href="https://fonts.googleapis.com/css2?family=Libre+Baskerville:wght@400;700&family=Nunito:wght@900&display=swap">
<style>
  :root {
    --band-green: #4ee11c;
    --band-green-light: #6cf23a;
    --rule-green: #1f7a12;
    --lawn-dark: #2f8f1a;
    --lawn-mid: #48b827;
    --lawn-light: #62cc35;
    --logo-green: #1e8c1e;
    --logo-yellow: #f2dc1a;
    --mower-grey: #6b6b6b;
    --mower-dark: #2a2a2a;
    --badge-orange: #f07a10;
    --badge-yellow: #ffd22a;
    --ink: #111111;
    --white: #ffffff;
  }
  * { box-sizing: border-box; margin: 0; padding: 0; }
  html, body { width: 1200px; height: 930px; overflow: hidden; background: #ffffff; }

  .postcard {
    position: relative;
    width: 1200px;
    height: 930px;
    overflow: hidden;
    background: var(--band-green);
    font-family: "Libre Baskerville", "Times New Roman", serif;
  }

  .top-band {
    position: absolute;
    left: 0; top: 0;
    width: 1200px; height: 206px;
    background: linear-gradient(180deg, var(--band-green-light), var(--band-green));
    border-bottom: 5px solid var(--rule-green);
    display: flex;
    flex-direction: column;
    align-items: center;
    justify-content: center;
  }
  .tagline {
    color: var(--white);
    font-weight: 700;
    font-size: 50px;
    line-height: 58px;
    letter-spacing: 1px;
    text-align: center;
    text-shadow: 3px 3px 0 var(--ink), -1px -1px 0 var(--ink), 1px -1px 0 var(--ink), -1px 1px 0 var(--ink);
  }

  .lawn-area {
    position: absolute;
    left: 0; top: 211px;
    width: 1200px; height: 538px;
    background:
      repeating-linear-gradient(100deg, rgba(255,255,255,0.07) 0 90px, rgba(0,0,0,0.06) 90px 180px),
      radial-gradient(ellipse at 50% 40%, var(--lawn-light), var(--lawn-mid) 55%, var(--lawn-dark));
  }

  .mower-illustration {
    position: absolute;
    left: 540px; top: 270px;
    width: 600px; height: 370px;
    border-radius: 120px 160px 140px 90px;
    background: radial-gradient(ellipse at 45% 45%, #8a8a8a, var(--mower-grey) 55%, var(--mower-dark));
    border: 5px solid var(--logo-yellow);
  }

  .brand-mark {
    position: absolute;
    left: 80px; top: 300px;
    display: flex;
    align-items: center;
    gap: 22px;
  }
  .brand-square {
    width: 70px; height: 70px;
    background: var(--logo-yellow);
  }
  .brand-name {
    font-family: "Libre Baskerville", "Times New Roman", serif;
    font-weight: 700;
    font-size: 130px;
    line-height: 1;
    color: var(--logo-yellow);
  }

  .price-badge {
    position: absolute;
    left: 940px; top: 190px;
    width: 190px; height: 190px;
  }
  .price-badge svg { position: absolute; inset: 0; }
  .price-badge .badge-text {
    position: absolute;
    inset: 0;
    display: flex;
    flex-direction: column;
    align-items: center;
    justify-content: center;
    color: var(--ink);
    text-align: center;
  }
  .badge-lead {
    font-size: 15px;
    font-weight: 700;
    line-height: 17px;
    margin-top: 6px;
  }
  .badge-price {
    font-size: 62px;
    font-weight: 700;
    line-height: 64px;
  }

  .other-services {
    position: absolute;
    left: 74px; top: 612px;
    color: var(--logo-yellow);
    text-transform: uppercase;
    text-shadow: 2px 2px 0 rgba(0,0,0,0.55);
  }
  .other-services h2 {
    font-size: 19px;
    font-weight: 400;
    line-height: 24px;
  }
  .other-services ul { list-style: none; }
  .other-services li {
    font-size: 26px;
    line-height: 33px;
  }

  .bottom-band {
    position: absolute;
    left: 0; top: 749px;
    width: 1200px; height: 181px;
    background: linear-gradient(180deg, var(--band-green), var(--band-green-light));
    border-top: 5px solid var(--rule-green);
    display: flex;
    flex-direction: column;
    align-items: center;
    justify-content: center;
    gap: 8px;
  }
  .phone-line {
    font-family: "Nunito", "Arial Rounded MT Bold", sans-serif;
    font-weight: 900;
    color: var(--white);
    font-size: 74px;
    line-height: 84px;
    text-shadow: 4px 4px 0 var(--ink), -1px -1px 0 var(--ink), 1px -1px 0 var(--ink), -1px 1px 0 var(--ink);
    display: flex;
    align-items: baseline;
    gap: 18px;
  }
  .phone-line .or {
    font-size: 34px;
  }
  .call-to-action {
    color: var(--ink);
    font-size: 35px;
    line-height: 40px;
    letter-spacing: 1px;
  }
</style>
</head>
<body>
  <main class="postcard">
    <header class="top-band">
      <p class="tagline">RELIABLE &amp; AFFORDABLE</p>
      <p class="tagline">COMMERCIAL &amp; RESIDENTIAL</p>
    </header>

    <section class="lawn-area" role="img" aria-label="Freshly mown striped lawn"></section>

    <div class="mower-illustration" role="img" aria-label="Cartoon lawn mower illustration"></div>

    <div class="brand-mark">
      <span class="brand-square"></span>
      <span class="brand-name">Brambo</span>
    </div>

    <div class="price-badge">
      <svg viewBox="-100 -100 200 200" width="190" height="190" aria-hidden="true">
        <defs>
          <radialGradient id="badgeGlow" cx="50%" cy="50%" r="50%">
            <stop offset="0%" stop-color="var(--badge-yellow)"/>
            <stop offset="100%" stop-color="var(--badge-orange)"/>
          </radialGradient>
        </defs>
        <polygon fill="url(#badgeGlow)" stroke="#c84f00" stroke-width="2"
          points="100,0 85,13.4 95.1,30.9 76.6,39 80.9,58.8 60.8,60.8 58.8,80.9 39,76.6 30.9,95.1 13.4,85 0,100 -13.4,85 -30.9,95.1 -39,76.6 -58.8,80.9 -60.8,60.8 -80.9,58.8 -76.6,39 -95.1,30.9 -85,13.4 -100,0 -85,-13.4 -95.1,-30.9 -76.6,-39 -80.9,-58.8 -60.8,-60.8 -58.8,-80.9 -39,-76.6 -30.9,-95.1 -13.4,-85 0,-100 13.4,-85 30.9,-95.1 39,-76.6 58.8,-80.9 60.8,-60.8 80.9,-58.8 76.6,-39 95.1,-30.9 85,-13.4"/>
      </svg>
      <div class="badge-text">
        <span class="badge-lead">PRICES START<br>FROM</span>
        <span class="badge-price">£10</span>
      </div>
    </div>

    <section class="other-services">
      <h2>Other services offered</h2>
      <ul>
        <li>Lawn treatment and</li>
        <li>Patio/drive cleaning</li>
        <li>Decking/fencing maintenance</li>
      </ul>
    </section>

    <footer class="bottom-band">
      <p class="phone-line">
        <span class="phone">01642385106</span>
        <span class="or">OR</span>
        <span class="phone">07481926053</span>
      </p>
      <p class="call-to-action">CALL TODAY FOR FREE ESTIMATE</p>
    </footer>
  </main>
</body>
</html>
```